Anselm business card

Business card for commercial photography , photographer specialized in advertising, architecture and interior photography, adventure imagery and camera work. 40 years old, worked for the last 20 years. Business card needs to convey a sense of confidence in work achieved. Card needs to be eye catching as will be left behind in many people's offices. Should also mention discreetly NLVG accredited photographer at the verso of the card. Phone number and website link must be apparent easily.

Target Market(s)

Advertising agencies, commercial photography representation

Industry/Entity Type

Architecture

Contact Information for Business Card

Phone number : +61 470 918 264
anselm.varnet@mailbrook.net
www.anselmvarnet.net

Font styles to use
Sans Serif

Requirements
Must have
• Email adress
• Website
• Phone number
• Name
• Photographer
Nice to have
• NLVG accredited photographer
Should not have
• Rond corners

```html
<!DOCTYPE html>
<html lang="en">
<head>
<meta charset="utf-8">
<title>Anselm Varnet – Business Card</title>
<link rel="stylesheet" href="https://fonts.googleapis.com/css2?family=Cinzel:wght@400;700&display=swap">
<style>
  :root {
    --page-bg: #d9d4ce;
    --frost-light: #f4f3f2;
    --frost-mid: #e3e1e0;
    --frost-warm: #e9d9da;
    --ink-dark: #3a3a3c;
    --panel-black: #0d0c0c;
    --panel-edge: #1c1b1b;
    --gold: #9a8467;
    --gold-soft: #7f6c55;
    --blue: #23407a;
    --badge-blue: #2c4f8f;
  }
  * { box-sizing: border-box; margin: 0; padding: 0; }
  html, body {
    width: 1200px;
    height: 970px;
    overflow: hidden;
    background: var(--page-bg);
    font-family: "Cinzel", serif;
  }
  .canvas {
    width: 1200px;
    height: 970px;
    display: flex;
    align-items: center;
    justify-content: center;
  }
  .card {
    width: 1000px;
    height: 556px;
    display: flex;
    box-shadow: 0 18px 40px rgba(0,0,0,0.25);
  }
  .card-front {
    width: 500px;
    height: 100%;
    background:
      radial-gradient(ellipse at 60% 80%, var(--frost-warm) 0%, transparent 55%),
      linear-gradient(180deg, var(--frost-light) 0%, var(--frost-mid) 100%);
    display: flex;
    align-items: center;
    justify-content: center;
  }
  .brand-name {
    font-size: 44px;
    font-weight: 400;
    color: var(--ink-dark);
    letter-spacing: 2px;
    white-space: nowrap;
  }
  .card-back {
    position: relative;
    flex: 1;
    height: 100%;
    background: linear-gradient(160deg, var(--panel-edge) 0%, var(--panel-black) 60%);
    padding: 134px 0 0 42px;
  }
  .holder-name {
    font-size: 25px;
    font-weight: 700;
    color: var(--gold);
    letter-spacing: 0.5px;
  }
  .holder-role {
    font-size: 20px;
    font-weight: 700;
    color: var(--blue);
    margin-top: -4px;
  }
  .contact-list {
    list-style: none;
    margin-top: 24px;
  }
  .contact-item {
    font-size: 22px;
    color: var(--gold);
    line-height: 40px;
  }
  .contact-item .label {
    color: var(--blue);
    font-weight: 700;
    margin-right: 6px;
  }
  .contact-email { font-size: 19px; }
  .website {
    margin-top: 20px;
    font-size: 19px;
    font-weight: 700;
    color: var(--blue);
  }
  .social-row {
    display: flex;
    align-items: center;
    gap: 16px;
    margin-top: 36px;
    color: var(--gold-soft);
  }
  .social-link {
    display: flex;
    align-items: center;
    gap: 8px;
    font-size: 18px;
  }
  .social-square {
    width: 36px;
    height: 36px;
    background: var(--gold-soft);
  }
  .contact-cta { font-size: 21px; }
  .accreditation-badge {
    position: absolute;
    right: 16px;
    bottom: 14px;
  }
</style>
</head>
<body>
<main class="canvas">
  <article class="card">
    <section class="card-front">
      <p class="brand-name">ANSELM VARNET</p>
    </section>
    <section class="card-back">
      <h1 class="holder-name">ANSELMVARNET</h1>
      <p class="holder-role">Photographer</p>
      <ul class="contact-list">
        <li class="contact-item"><span class="label">P:</span>+61 470 918 264</li>
        <li class="contact-item contact-email"><span class="label">E:</span>anselm.varnet@mailbrook.net</li>
      </ul>
      <p class="website">www.anselmvarnet.net</p>
      <div class="social-row">
        <span class="social-link"><span class="social-square"></span>Folio</span>
        <span class="social-link"><span class="social-square"></span>Chirp</span>
        <span class="contact-cta">Contact Me</span>
      </div>
      <svg class="accreditation-badge" width="78" height="78" viewBox="0 0 78 78" role="img" aria-label="NLVG accreditation badge">
        <circle cx="39" cy="39" r="38" fill="var(--badge-blue)" opacity="0.85"/>
      </svg>
    </section>
  </article>
</main>
</body>
</html>
```